Brocure for Brindle - Social Media Management

Brindle is a Dutch company in the market of Social Media growth. We need a brochure (digital/PDF) for our company. Please see attached word doc for the text and attached logo. The initial proposal can contain just the first 4 pages text of the word doc.

We use informal language in all our communication.

Slogan: Effectieve Social Media Marketing voor professionals en ondernemers

Website: brindlesm-voorbeeld.nl

Industry/Entity Type

Digital Marketing

Contact Information for Business Card

Contact details:

Gerrit ter Hoeve
gerrit@brindlesm-voorbeeld.nl
06-19573826

```html
<!DOCTYPE html>
<html lang="nl">
<head>
<meta charset="utf-8">
<title>Brindle – brochure</title>
<link rel="stylesheet" href="https://fonts.googleapis.com/css2?family=Montserrat:wght@400;500;600;700;800&family=Open+Sans:wght@400;600;700&display=swap">
<style>
  :root {
    --orange: #e0531a;
    --orange-dark: #c9461170;
    --navy: #1d2f4f;
    --grey: #efefef;
    --paper: #ffffff;
    --text: #3a3a3a;
    --stage: #e4e4e7;
  }
  * { box-sizing: border-box; margin: 0; padding: 0; }
  html, body { width: 1200px; height: 2271px; overflow: hidden; }
  body { background: var(--stage); font-family: "Open Sans", sans-serif; color: var(--text); position: relative; }

  .spread { position: absolute; left: 80px; width: 1040px; height: 735px; display: flex; box-shadow: 0 6px 22px rgba(0,0,0,.12); }
  .spread--cover { top: 16px; }
  .spread--inside-a { top: 767px; }
  .spread--inside-b { top: 1518px; }

  .page { position: relative; width: 520px; height: 735px; background: var(--paper); overflow: hidden; }
  .page + .page { border-left: 1px solid #e2e2e2; }
  .page-art { position: absolute; inset: 0; width: 100%; height: 100%; }

  /* brand name */
  .brand { display: flex; align-items: center; gap: 8px; font-family: "Montserrat", sans-serif; font-weight: 800; color: var(--orange); text-transform: uppercase; letter-spacing: .04em; }
  .brand__dot { border-radius: 50%; background: var(--orange); flex: none; }

  /* back cover */
  .back-brand { position: absolute; left: 58px; top: 318px; font-size: 30px; }
  .back-brand .brand__dot { width: 26px; height: 26px; }
  .contact { position: absolute; left: 58px; top: 392px; font-family: "Montserrat", sans-serif; color: var(--navy); }
  .contact__title { font-size: 20px; font-weight: 700; }
  .contact__rule { width: 92px; height: 3px; background: var(--navy); margin: 6px 0 18px; }
  .contact__row { display: flex; align-items: center; gap: 14px; font-size: 14px; font-weight: 700; margin-bottom: 12px; }
  .contact__row svg { width: 18px; height: 18px; flex: none; }

  /* front cover */
  .front-brand { position: absolute; left: 70px; top: 368px; font-size: 26px; }
  .front-brand .brand__dot { width: 22px; height: 22px; }
  .cover-title { position: absolute; left: 46px; top: 430px; font-family: "Montserrat", sans-serif; font-weight: 800; color: var(--orange); font-size: 50px; line-height: 1; letter-spacing: .01em; text-transform: uppercase; }
  .cover-slogan { position: absolute; left: 46px; top: 548px; font-family: "Montserrat", sans-serif; font-size: 18px; color: var(--navy); font-weight: 500; }
  .cover-rule { position: absolute; left: 46px; top: 584px; width: 190px; height: 5px; background: var(--orange); }
  .cover-url { position: absolute; left: 46px; top: 612px; font-family: "Montserrat", sans-serif; font-size: 19px; font-weight: 700; color: var(--navy); letter-spacing: .12em; }

  /* inside pages */
  .band { padding: 12px 40px; }
  .band--grey { background: var(--grey); }
  .band--top { padding-top: 38px; }
  .page-heading { font-family: "Montserrat", sans-serif; font-weight: 800; color: var(--orange); text-transform: uppercase; font-size: 17px; line-height: 1.25; margin-bottom: 12px; }
  .section-title { font-family: "Montserrat", sans-serif; font-weight: 700; color: var(--navy); font-size: 14px; margin-bottom: 5px; }
  .section-lead { font-family: "Montserrat", sans-serif; font-weight: 700; color: var(--orange); font-size: 10px; margin-bottom: 10px; }
  .body { font-size: 9.5px; line-height: 1.5; margin-bottom: 5px; }
  .body--strong { font-weight: 700; color: var(--navy); }

  .platforms { display: grid; grid-template-columns: 1.6fr 1fr; gap: 6px 16px; }
  .platform { display: flex; align-items: center; gap: 8px; font-size: 8.5px; font-weight: 700; color: #222; line-height: 1.25; }
  .platform__icon { width: 17px; height: 17px; border-radius: 50%; background: var(--navy); flex: none; }

  .ribbon { position: absolute; right: 0; top: 355px; width: 200px; height: 30px; background: var(--orange); color: #fff; font-family: "Montserrat", sans-serif; font-weight: 700; font-size: 15px; display: flex; align-items: center; padding-left: 28px; clip-path: polygon(0 0, 100% 0, 100% 100%, 0 100%, 14px 50%); }

  .photo-block { position: absolute; left: 40px; right: 40px; top: 330px; height: 325px; background: linear-gradient(140deg, #1c4f8c, #2a78c4 45%, #143a6b); }

  /* footer */
  .foot-brand { position: absolute; left: 40px; bottom: 34px; font-size: 13px; gap: 5px; }
  .foot-brand .brand__dot { width: 11px; height: 11px; }
  .foot-line { position: absolute; left: 130px; right: 175px; bottom: 30px; height: 1px; background: var(--navy); }
  .foot-pill { position: absolute; right: 44px; bottom: 20px; height: 22px; padding: 0 22px 0 16px; border-radius: 11px 0 0 11px; background: var(--navy); color: #fff; font-family: "Montserrat", sans-serif; font-size: 10px; letter-spacing: .08em; display: flex; align-items: center; }
  .foot-num { position: absolute; right: 28px; bottom: 17px; width: 28px; height: 28px; border-radius: 50%; background: var(--orange); color: #fff; font-family: "Montserrat", sans-serif; font-weight: 700; font-size: 10px; display: flex; align-items: center; justify-content: center; }
</style>
</head>
<body>

<!-- Spread: back and front cover -->
<section class="spread spread--cover">
  <div class="page page--back">
    <svg class="page-art" viewBox="0 0 520 735" aria-hidden="true">
      <rect width="520" height="735" fill="#e0531a"/>
      <circle cx="270" cy="170" r="115" fill="none" stroke="#c94611" stroke-width="14" opacity=".5"/>
      <text x="270" y="180" text-anchor="middle" font-family="Montserrat, sans-serif" font-weight="800" font-size="30" fill="#c94611" opacity=".5">BRINDLE</text>
      <circle cx="110" cy="625" r="345" fill="#ffffff"/>
    </svg>
    <div class="brand back-brand"><span class="brand__dot"></span>Brindle</div>
    <div class="contact">
      <div class="contact__title">Contact us</div>
      <div class="contact__rule"></div>
      <div class="contact__row">
        <svg viewBox="0 0 24 24"><path fill="#e0531a" d="M6.6 10.8a15 15 0 0 0 6.6 6.6l2.2-2.2c.3-.3.7-.4 1-.2 1.1.4 2.3.6 3.6.6.6 0 1 .4 1 1V20c0 .6-.4 1-1 1A17 17 0 0 1 3 4c0-.6.4-1 1-1h3.5c.6 0 1 .4 1 1 0 1.3.2 2.5.6 3.6.1.3 0 .7-.2 1z"/></svg>
        06-19573826
      </div>
      <div class="contact__row">
        <svg viewBox="0 0 24 24"><rect x="2" y="5" width="20" height="14" rx="2" fill="#e0531a"/><path d="M3 6l9 7 9-7" fill="none" stroke="#fff" stroke-width="1.6"/></svg>
        gerrit@brindlesm-voorbeeld.nl
      </div>
      <div class="contact__row">
        <svg viewBox="0 0 24 24"><circle cx="12" cy="12" r="10" fill="#e0531a"/><path d="M2 12h20M12 2c3 3 3 17 0 20M12 2c-3 3-3 17 0 20" fill="none" stroke="#fff" stroke-width="1.4"/></svg>
        www.brindlesm-voorbeeld.nl
      </div>
    </div>
  </div>

  <div class="page page--front">
    <svg class="page-art" viewBox="0 0 520 735" aria-hidden="true">
      <circle cx="405" cy="55" r="352" fill="#e0531a"/>
      <circle cx="405" cy="55" r="346" fill="#ffffff"/>
      <circle cx="405" cy="55" r="342" fill="#1d2f4f"/>
    </svg>
    <svg class="page-art" viewBox="0 0 520 735" role="img" aria-label="Foto: drie jonge mensen op een bank die op hun telefoon kijken">
      <defs>
        <linearGradient id="photoTone" x1="0" y1="0" x2="1" y2="1">
          <stop offset="0" stop-color="#f1efec"/>
          <stop offset=".6" stop-color="#d9d3cc"/>
          <stop offset="1" stop-color="#8a8f9c"/>
        </linearGradient>
      </defs>
      <circle cx="405" cy="55" r="333" fill="url(#photoTone)"/>
    </svg>
    <svg class="page-art" viewBox="0 0 520 735" aria-hidden="true" font-family="Montserrat, sans-serif" font-size="15" fill="#555">
      <g transform="translate(160 95)">
        <rect width="82" height="26" rx="3" fill="#fff"/>
        <path d="M12 18l-6-6a3.5 3.5 0 0 1 6-3.5A3.5 3.5 0 0 1 18 12z" fill="#e8607a"/><text x="22" y="18">25</text>
        <path d="M50 8h16a3 3 0 0 1 3 3v5a3 3 0 0 1-3 3h-10l-4 3v-3a3 3 0 0 1-2-3v-5a3 3 0 0 1 3-3z" fill="#3b8fd6"/><text x="72" y="18" font-size="13">9</text>
      </g>
      <g transform="translate(330 110)">
        <rect width="44" height="26" rx="3" fill="#fff"/>
        <path d="M8 8h16a3 3 0 0 1 3 3v5a3 3 0 0 1-3 3h-10l-4 3v-3a3 3 0 0 1-2-3v-5a3 3 0 0 1 3-3z" fill="#3b8fd6"/><text x="31" y="18">9</text>
      </g>
      <g transform="translate(420 135)">
        <rect width="90" height="26" rx="3" fill="#fff"/>
        <path d="M12 18l-6-6a3.5 3.5 0 0 1 6-3.5A3.5 3.5 0 0 1 18 12z" fill="#e8607a"/><text x="22" y="18">25</text>
        <circle cx="60" cy="9" r="3.5" fill="#2bb3a6"/><path d="M54 19a6 6 0 0 1 12 0z" fill="#2bb3a6"/><text x="70" y="18">3</text>
      </g>
    </svg>
    <div class="brand front-brand"><span class="brand__dot"></span>Brindle</div>
    <h1 class="cover-title">Effectieve<br>Social Media</h1>
    <p class="cover-slogan">Marketing voor professionals en ondernemers</p>
    <div class="cover-rule"></div>
    <p class="cover-url">www.brindlesm-voorbeeld.nl</p>
  </div>
</section>

<!-- Spread: pages 1 and 2 -->
<section class="spread spread--inside-a">
  <div class="page">
    <div class="band band--top">
      <h2 class="page-heading">Social media marketing voor zakelijke professionals en ondernemers</h2>
      <h3 class="section-title">Groei, interactie en content</h3>
      <p class="body">Je bereik vergroten, traffic genereren en daarmee meer omzet behalen. Dat is wat wij beogen. Onze formule is simpel: met een slimme strategie en relevante content zorgen we voor echte interactie op je sociale netwerken.</p>
      <p class="body body--strong">(actieve interactie + relevante content) &gt; actieve volgers) = (&gt; traffic + omzet)</p>
    </div>
    <div class="band band--grey">
      <h3 class="section-title">Wie zijn wij?</h3>
      <p class="body">Wij zijn Brindle. Een team van social media experts dat je sociale netwerk activeert en het bereik vergroot. We zorgen voor interactie met volgers, zetten je bedrijf op de kaart en genereren traffic naar je website of webshop.</p>
      <p class="body body--strong">Het doel? Meer omzet. Simpel en heel meetbaar.</p>
      <h3 class="section-title">Voor wie?</h3>
      <p class="body">Onze dienstverlening kan ingezet worden op zowel persoonlijke zakelijke profielen (bv. Netwerkr) of voor bedrijfspagina's op diverse sociale mediakanalen.</p>
    </div>
    <div class="band">
      <h3 class="section-title">Wat doen we?</h3>
      <p class="body">Samen met jou bepalen we je doelen in de sociale netwerken. Zowel strategisch als tactisch en operationeel. Wij richten ons op de doelgroep en zorgen voor een netwerk van echte en actieve volgers. Of het nu gaat om Netwerkr, Fotogram, Vriendenboek of Kwetter: interactie zorgt voor betrokken volgers.</p>
      <p class="body">Voor zakelijke professionals verzorgen we persoonlijke branding, zodat jij gezien wordt als autoriteit in je vakgebied. Onze diensten voor bedrijven bestaan uit de organische groei van je netwerk en het activeren van dat netwerk met content en interactie. Zo vinden meer bezoekers hun weg naar je website.</p>
    </div>
    <div class="brand foot-brand"><span class="brand__dot"></span>Brindle</div>
    <div class="foot-line"></div>
    <div class="foot-pill">www.brindlesm-voorbeeld.nl</div>
    <div class="foot-num">01</div>
  </div>

  <div class="page">
    <div class="band band--grey band--top">
      <h3 class="section-title">Welke platformen?</h3>
      <p class="section-lead">We bieden onze diensten aan op alle belangrijke platformen:</p>
      <div class="platforms">
        <div class="platform"><span class="platform__icon"></span>Netwerkr (bedrijfspagina's en persoonlijke profielen)</div>
        <div class="platform"><span class="platform__icon"></span>Kwetter</div>
        <div class="platform"><span class="platform__icon"></span>Vriendenboek (bedrijfspagina's en groepen)</div>
        <div class="platform"><span class="platform__icon"></span>Kijkbuis</div>
        <div class="platform"><span class="platform__icon"></span>Fotogram (bedrijfspagina's en persoonlijke profielen)</div>
        <div class="platform"><span class="platform__icon"></span>Zoekkaart Bedrijf</div>
        <div class="platform"><span class="platform__icon"></span>Optioneel: Klipklok, Prikbord, Draadforum en Blogrol</div>
      </div>
    </div>
    <div class="band">
      <h3 class="section-title">Waarom kies je voor ons?</h3>
      <p class="body">Jij hebt jouw vak, wij het onze. Als iedereen doet waar hij goed in is, worden we daar allemaal beter van. Wij zijn goed in het activeren en vergroten van je sociale netwerk. Daarvoor gebruiken we een slimme mix van kennis en tools.</p>
      <p class="body">Een strategie die ervoor zorgt dat jij je kunt focussen op je corebusiness. Met onze slimme tools vergroten wij de impact van je sociale netwerken. Met als resultaat: meer traffic, meer leads, meer omzet.</p>
    </div>
    <div class="band band--grey">
      <h3 class="section-title">Hoe lang gaan we met elkaar in zee?</h3>
      <p class="body">Een groeistrategie werkt op de lange termijn het beste als die groei organisch is. En dat vraagt dus ook een strategie voor de lange termijn. Lang is relatief, maar reken erop dat we minimaal een jaar nodig hebben om de groeistrategie optimaal te laten werken. Natuurlijk is er in elke situatie snelle winst te behalen. Maar voor een goede samenwerking is het belangrijk dat je elkaar leert kennen en begrijpen. Daarom vragen we ook regelmatig jouw energie en input.</p>
    </div>
    <div class="band">
      <h3 class="section-title">Groeien op sociale media</h3>
      <p class="body">Het staat als een paal boven water: sociale media zijn een krachtig marketinginstrument. Een kans die je niet voorbij kunt laten gaan, of je dat nou leuk vindt of niet. Het geeft je de kans om je merk op te bouwen, je zicht- en vindbaarheid te verbeteren en meer leads en verkopen te genereren. Het beheren van je sociale platforms is een tijdrovende klus. En om resultaat te krijgen, moet je het ook nog eens slim doen.</p>
    </div>
    <div class="brand foot-brand"><span class="brand__dot"></span>Brindle</div>
    <div class="foot-line"></div>
    <div class="foot-pill">www.brindlesm-voorbeeld.nl</div>
    <div class="foot-num">01</div>
  </div>
</section>

<!-- Spread: pages 3 and 4 -->
<section class="spread spread--inside-b">
  <div class="page">
    <div class="band band--top">
      <h3 class="section-title">Volledig social management</h3>
      <p class="body">We bieden een compleet beheerpakket voor je sociale media waarmee je de betrokkenheid van volgers vergroot. We schakelen altijd proactief naar de volgende stap, zodat jouw kanalen in goede handen zijn. We plannen, posten, delen en reageren, zodat jouw merk dagelijks zichtbaar blijft.</p>
    </div>
    <div class="band band--grey">
      <h3 class="section-title">Volledig sociaal management</h3>
      <p class="body">Je bent al een poos bezig met het beheren van je sociale media, maar ziet geen commercieel resultaat? Onze specialisten analyseren je kanalen en maken een plan dat wel werkt. Zo krijg je meer likes, meer interactie en meer betrokken volgers die klant worden.</p>
    </div>
    <div class="band">
      <h3 class="section-title">Groeistrategie</h3>
      <p class="body">Wij stellen een strategie op die past bij jouw doelen en doelgroep. Met de juiste content en de juiste timing groeit je netwerk organisch en gestaag, en levert het meer bezoekers en leads op.</p>
    </div>
    <div class="ribbon">Hoe werkt het?</div>
    <div class="band band--grey" style="margin-top:34px">
      <h3 class="section-title">Quick Scan&amp; advies</h3>
      <p class="body">We starten altijd met een grondige analyse van je website en sociale kanalen. Op basis daarvan geven we je een helder advies over de beste aanpak.</p>
      <h3 class="section-title">Je wilt met ons in zee</h3>
      <p class="body">Besluit je met ons in zee te gaan, dan doen we dat niet voor een paar weken. We bouwen samen aan je netwerk en maken duidelijke afspraken over doelen, planning en rapportage.</p>
      <h3 class="section-title">Pakketkeuze</h3>
      <p class="body">We hebben verschillende pakketten, zodat je kunt kiezen wat bij jouw situatie en wensen past. Geen vaste kosten vooraf, gewoon een helder maandbedrag.</p>
    </div>
    <div class="brand foot-brand"><span class="brand__dot"></span>Brindle</div>
    <div class="foot-line"></div>
    <div class="foot-pill">www.brindlesm-voorbeeld.nl</div>
    <div class="foot-num">03</div>
  </div>

  <div class="page">
    <div class="band band--top">
      <h3 class="section-title">Implementatie</h3>
      <p class="body">Natuurlijk wil je zo snel mogelijk resultaat zien. Dat willen wij ook. We werken de strategie uit in een plan en gaan voor jou aan het werk, met prioriteit op de gebieden die zo snel mogelijk resultaten opleveren. Omdat we graag laten zien dat onze inspanningen verschil maken. We richten daarvoor de benodigde systemen in. In het begin hebben we regelmatig overleg om elkaar goed te leren kennen en de vinger aan de pols te houden.</p>
    </div>
    <div class="band band--grey">
      <h3 class="section-title">Terugkoppeling en verbetering</h3>
      <p class="body">Iedere ondernemer is gedreven als het gaat om het behalen van resultaten. Zo ook wij. Wij doen er alles aan om onze dienstverlening zo succesvol mogelijk te laten zijn en jouw sociale doelen te behalen. We hebben regelmatig contact om de resultaten te bespreken en daar waar mogelijk te verbeteren.</p>
    </div>
    <div class="photo-block" role="img" aria-label="Foto: gekleurde blokjes met pictogrammen van sociale netwerken op een blauwe ondergrond"></div>
    <div class="brand foot-brand"><span class="brand__dot"></span>Brindle</div>
    <div class="foot-line"></div>
    <div class="foot-pill">www.brindlesm-voorbeeld.nl</div>
    <div class="foot-num">04</div>
  </div>
</section>

</body>
</html>
```